Company letter head and business card for new Indian Pharmaceutical Export company.

We need a letterhead and business card design for an Indian Pharmaceutical Export company.

The letter head needs to contain the following information.
Verona Healthline Pvt. Ltd.
Office No 4837 Plot No 52, Kestrel Heights, RT Lane, 400517, Maharashtra, India.
Email: info@verona-healthline.example
Phone: +91-8213460592
CIN: U58213MH2025PTC719264
GSTIN: (This number is still pending, we will add later)

The business card needs to contain:
Address:
Verona Healthline Pvt. Ltd.
Office No 4837 Plot No52, Kestrel Heights, RT Lane, 400517, MH, India.
Email: tobias@verona-healthline.example
Phone: +49-17638421956
Name on card: Tobias Wendlinger
Position: Director

The design for the letter head and business card should be simple but trustworthy.
Please use only Green and blue, same as in the attached logo.

```html
<!DOCTYPE html>
<html lang="en">
<head>
<meta charset="utf-8">
<title>Verona Healthline – Stationery Set</title>
<link href="https://fonts.googleapis.com/css2?family=Lexend:wght@300;400;500&family=Montserrat:wght@700&display=swap" rel="stylesheet">
<style>
  :root{
    --blue:#1b75bc;
    --blue-deep:#0a5fa8;
    --blue-faint:#c4dbee;
    --green:#8dc63f;
    --green-faint:#e1efcf;
    --ink:#1c1c1c;
    --paper:#ffffff;
    --bg:#ffffff;
    --shadow:0 14px 30px rgba(0,0,0,.28);
  }
  *{box-sizing:border-box;margin:0;padding:0}
  html,body{width:1200px;height:1200px;overflow:hidden;background:var(--bg)}
  body{position:relative;font-family:'Lexend',sans-serif;color:var(--ink)}
  .sheet{position:absolute;background:var(--paper);box-shadow:var(--shadow);overflow:hidden}

  .brand{position:absolute;display:flex;flex-direction:column;align-items:center;transform:translateX(-50%)}
  .brand-dot{border-radius:50%;background:var(--green)}
  .brand-name{font-family:'Montserrat',sans-serif;font-weight:700;color:var(--blue-deep);white-space:nowrap}

  .legal{position:absolute;font-size:9.5px;font-weight:400;right:14px}

  /* business card back */
  .divider{position:absolute;left:177px;top:55px;width:1.5px;height:124px;background:var(--ink)}
  .watermark{position:absolute;border-radius:50%;background:linear-gradient(160deg,var(--blue-faint) 0%,var(--blue-faint) 45%,var(--green-faint) 70%);opacity:.55}
  .card-person{position:absolute;left:212px;top:58px}
  .card-person .name{font-size:18.5px;font-weight:500;line-height:1.1}
  .card-person .role{font-size:11.5px;font-weight:500}
  .contacts{list-style:none;position:absolute;font-size:9.4px;font-weight:300}
  .contacts li{display:flex;align-items:flex-start;gap:8px;margin-bottom:6px;line-height:1.2}
  .icon{width:12px;height:12px;flex:none}
  .phone-num{letter-spacing:1.2px}

  /* letterhead */
  .lh-rule{position:absolute;left:47px;top:112px;width:331px;height:1.5px;background:var(--blue-deep)}
  .lh-body{position:absolute;left:53px;top:132px;width:325px;font-size:10.3px;font-weight:300;line-height:1.2}
  .lh-body .rec-name{font-size:14.5px;font-weight:500;line-height:1.1}
  .lh-body .rec-title{font-weight:500}
  .lh-body .gap{margin-top:10px}
  .lh-body p{text-align:justify;margin-bottom:4px}
  .lh-body .salute{font-weight:500;margin-top:12px}
  .lh-from{position:absolute;left:53px;top:427px;font-size:10.3px;font-weight:300}
  .lh-from .name{font-size:13.5px;font-weight:500;line-height:1.1}
  .lh-from .role{font-size:8.5px;font-weight:500}
  .signature{position:absolute;left:53px;top:490px;font-size:10.3px;font-weight:300}
  .signature::before{content:"";position:absolute;left:0;top:-4px;width:76px;border-top:1px solid var(--ink)}
  .lh-contacts{right:60px;top:432px;text-align:right}
  .lh-contacts li{justify-content:flex-end;margin-bottom:6px}
  .lh-contacts .cin{font-weight:400}

  .envelope-flap{position:absolute;left:0;top:0;width:390px;height:60px}
</style>
</head>
<body>

<!-- Card front -->
<section class="sheet card-front" style="left:129px;top:89px;width:409px;height:234px">
  <div class="brand" style="left:205px;top:62px">
    <div class="brand-dot" style="width:82px;height:82px"></div>
    <div class="brand-name" style="font-size:13px;margin-top:14px">Verona Healthline</div>
  </div>
  <div class="legal" style="bottom:10px">Verona Healthline Pvt. Ltd.</div>
</section>

<!-- Card back -->
<section class="sheet card-back" style="left:669px;top:89px;width:410px;height:234px">
  <div class="watermark" style="left:188px;top:10px;width:210px;height:210px"></div>
  <div class="brand" style="left:89px;top:56px">
    <div class="brand-dot" style="width:82px;height:82px"></div>
    <div class="brand-name" style="font-size:13px;margin-top:14px">Verona Healthline</div>
  </div>
  <div class="divider"></div>
  <div class="card-person">
    <div class="name">Tobias Wendlinger</div>
    <div class="role">Director</div>
  </div>
  <ul class="contacts" style="left:212px;top:105px">
    <li><svg class="icon" viewBox="0 0 12 12"><circle cx="6" cy="6" r="6" fill="#1c1c1c"/><path d="M4 3.2l1 1.4-.6.7c.4.9 1.1 1.6 2 2l.7-.6 1.4 1-.6 1C6.2 8.7 3.4 5.9 3.2 4z" fill="#fff"/></svg><span class="phone-num">+49-17638421956</span></li>
    <li><svg class="icon" viewBox="0 0 12 12"><circle cx="6" cy="6" r="6" fill="#1c1c1c"/><rect x="3.2" y="4" width="5.6" height="4" fill="#fff"/><path d="M3.2 4L6 6.2 8.8 4" stroke="#1c1c1c" stroke-width=".6" fill="none"/></svg><span>tobias@verona-healthline.example</span></li>
    <li><svg class="icon" viewBox="0 0 12 12"><path d="M6 0a4.5 4.5 0 0 1 4.5 4.5C10.5 8 6 12 6 12S1.5 8 1.5 4.5A4.5 4.5 0 0 1 6 0z" fill="#1c1c1c"/><circle cx="6" cy="4.5" r="1.7" fill="#fff"/></svg><span>Office No 4837 Plot No52,<br>Kestrel Heights, RT Lane,<br>400517, MH, India.</span></li>
  </ul>
</section>

<!-- Cover sheet -->
<section class="sheet cover" style="left:129px;top:354px;width:432px;height:556px">
  <div class="brand" style="left:216px;top:180px">
    <div class="brand-dot" style="width:132px;height:132px"></div>
    <div class="brand-name" style="font-size:17px;margin-top:18px">Verona Healthline</div>
  </div>
  <div class="legal" style="right:28px;bottom:18px">Verona Healthline Pvt. Ltd.</div>
</section>

<!-- Letterhead -->
<section class="sheet letterhead" style="left:639px;top:354px;width:432px;height:556px">
  <div class="watermark" style="left:118px;top:146px;width:245px;height:245px"></div>
  <div class="brand" style="left:87px;top:30px">
    <div class="brand-dot" style="width:58px;height:58px"></div>
    <div class="brand-name" style="font-size:8.5px;margin-top:10px">Verona Healthline</div>
  </div>
  <div class="lh-rule"></div>
  <div class="lh-body">
    <div>To.</div>
    <div class="rec-name">Recipient's Name</div>
    <div class="rec-title">Title</div>
    <div class="gap">Company Name</div>
    <div>Your Address Here<br>Your Phone Number</div>
    <div class="salute">Dear Sir</div>
    <p>There are many variations of passages of Lorem Ipsum available, but the majority have suffered alteration in some form, by injected humour, or randomised words which don't look even slightly believable. If you are going to use a passage of Lorem Ipsum, you need to be sure there isn't anything embarrassing hidden in the middle of text.</p>
    <p>All the Lorem Ipsum generators on the Internet tend to repeat predefined chunks as necessary, making this the first true generator on the Internet. It uses a dictionary of over 200 Latin words, combined with a handful of model sentence structures, to generate Lorem Ipsum which looks reasonable.</p>
    <p>The generated Lorem Ipsum is therefore always free from repetition, injected humour, or non-characteristic words etc</p>
  </div>
  <div class="lh-from">
    <div>From.</div>
    <div class="name">Tobias Wendlinger</div>
    <div class="role">Director</div>
  </div>
  <div class="signature">Signature</div>
  <ul class="contacts lh-contacts">
    <li><span class="phone-num">+91-8213460592</span><svg class="icon" viewBox="0 0 12 12"><circle cx="6" cy="6" r="6" fill="#1c1c1c"/><path d="M4 3.2l1 1.4-.6.7c.4.9 1.1 1.6 2 2l.7-.6 1.4 1-.6 1C6.2 8.7 3.4 5.9 3.2 4z" fill="#fff"/></svg></li>
    <li><span>info@verona-healthline.example</span><svg class="icon" viewBox="0 0 12 12"><circle cx="6" cy="6" r="6" fill="#1c1c1c"/><rect x="3.2" y="4" width="5.6" height="4" fill="#fff"/><path d="M3.2 4L6 6.2 8.8 4" stroke="#1c1c1c" stroke-width=".6" fill="none"/></svg></li>
    <li><span>Office No 4837 Plot No 52,<br>Kestrel Heights, RT Lane,<br>400517, Maharashtra, India.</span><svg class="icon" viewBox="0 0 12 12"><path d="M6 0a4.5 4.5 0 0 1 4.5 4.5C10.5 8 6 12 6 12S1.5 8 1.5 4.5A4.5 4.5 0 0 1 6 0z" fill="#1c1c1c"/><circle cx="6" cy="4.5" r="1.7" fill="#fff"/></svg></li>
    <li class="cin"><span>CIN: U58213MH2025PTC719264</span><span class="icon"></span></li>
  </ul>
</section>

<!-- Envelope front -->
<section class="sheet envelope-front" style="left:129px;top:944px;width:390px;height:175px">
  <div class="brand" style="left:195px;top:38px">
    <div class="brand-dot" style="width:62px;height:62px"></div>
    <div class="brand-name" style="font-size:9px;margin-top:10px">Verona Healthline</div>
  </div>
  <div class="legal" style="right:22px;bottom:10px">Verona Healthline Pvt. Ltd.</div>
</section>

<!-- Envelope back -->
<section class="sheet envelope-back" style="left:681px;top:944px;width:390px;height:175px">
  <svg class="envelope-flap" viewBox="0 0 390 60" aria-hidden="true">
    <path d="M0 0H390L381 50Q379 59 370 59H20Q11 59 9 50Z" fill="var(--blue)"/>
  </svg>
</section>

</body>
</html>
```